TGCo Wholesale Flyer

I need a wholesaler flyer/letter put together. I've provided copy and a range of photos for the designer to use. The flyer needs to match the same colour pallet and style of tallowmeregoodsco.com.au.

It will be used to send to new potenial retailers so needs to look smick.

```html
<!DOCTYPE html>
<html lang="en">
<head>
<meta charset="utf-8">
<title>Tallowmere Goods Co. — Wholesale Flyer</title>
<link rel="stylesheet" href="https://fonts.googleapis.com/css2?family=Marcellus&family=Figtree:wght@400&display=swap">
<style>
  :root {
    --page: #ffffff;
    --paper: #e1e0dc;
    --rule: #8c8c8a;
    --ink: #2a2a28;
    --ink-soft: #3a3a38;
    --on-photo: #ffffff;
    --sky: #d8d7d2;
    --hill: #8d8767;
    --foliage: #58593a;
    --sandstone: #b59666;
    --road: #7a766e;
  }
  * { box-sizing: border-box; margin: 0; padding: 0; }
  html, body { width: 1200px; height: 1200px; overflow: hidden; background: var(--page); }
  .flyer {
    position: absolute; left: 86px; top: 236px;
    width: 1036px; height: 736px;
    display: flex; border: 1px solid var(--rule);
  }
  .story {
    position: relative; width: 517px; height: 100%;
    background: var(--paper); border-right: 1px solid var(--rule);
    color: var(--ink-soft);
    font-family: "Figtree", sans-serif;
  }
  .story-title {
    position: absolute; left: 45px; top: 32px;
    font-family: "Marcellus", serif; font-weight: 400;
    font-size: 15px; line-height: 16px; color: var(--ink);
    text-transform: uppercase; letter-spacing: 0.2px;
  }
  .story-body {
    position: absolute; left: 45px; top: 70px; width: 436px;
    font-size: 10.4px; line-height: 15px;
  }
  .story-body p { margin-bottom: 15px; }
  .brand-inline { font-family: "Marcellus", serif; font-size: 11.5px; color: var(--ink); }
  .founders-photo {
    float: right; width: 202px; height: 201px; margin: 0 0 6px 6px;
    background: linear-gradient(180deg, #efefef 0%, #a9a9a9 22%, #6f6f6f 45%, #8a8a8a 70%, #5e5e5e 100%);
  }
  .brand-mark {
    position: absolute; left: 51px; top: 608px; width: 200px;
    text-align: center; font-family: "Marcellus", serif;
    font-size: 27px; line-height: 25px; color: var(--ink);
  }
  .contact {
    position: absolute; left: 298px; top: 606px;
    list-style: none; font-size: 12px; line-height: 16px; color: var(--ink);
  }
  .contact li { display: flex; gap: 8px; margin-bottom: 11px; }
  .contact svg { width: 12px; height: 12px; flex: none; margin-top: 2px; }
  .shopfront {
    position: relative; flex: 1; height: 100%;
    background:
      linear-gradient(180deg, var(--sky) 0%, var(--sky) 22%, var(--hill) 32%, var(--foliage) 44%, var(--sandstone) 58%, #9c835d 72%, var(--road) 76%, #9a958b 100%);
  }
  .shopfront-title {
    position: absolute; left: 0; right: 0; top: 548px;
    text-align: center; font-family: "Marcellus", serif; font-weight: 400;
    font-size: 54px; line-height: 48px; color: var(--on-photo);
  }
</style>
</head>
<body>
  <main class="flyer">
    <section class="story">
      <h1 class="story-title">Tallowmere Goods Co.<br>Our Story</h1>
      <div class="story-body">
        <div class="founders-photo" role="img" aria-label="Black and white photo of the two founders embracing in a field with hills behind"></div>
        <p><span class="brand-inline">TALLOWMERE GOODS CO.</span> is a small, family-owned business based on our property, Hollowmead Farm, in historic Richmond, Tasmania. Since 2014, we’ve been creating Tasmanian botanical products that reflect the beauty and simplicity of where we live.</p>
        <p>We handcraft our candles, diffusers, room mists and body products in small batches on the farm. Each product begins with natural ingredients that we grow ourselves or source locally when we can, like calendula, chamomile, rose, rosemary, Tasmanian blue gum and organic Tasmanian seaweed.</p>
        <p>Our candles are poured by hand using natural soy wax and cotton wicks. Their scents are inspired by the Tasmanian landscape. Our diffusers and room mists are blended slowly to create a clean, steady fragrance. And our soaps and body products are created using artisanal methods and botanicals known for their soothing properties.</p>
        <p>Richmond’s history shapes everything we do at TGCo. Australia’s oldest bridge and the village’s heritage streets remind us to take our time, keep things simple and make products that feel honest and meaningful.</p>
        <p>We minimise single-use plastics and create with care for people and the planet. And we are proudly cruelty free.</p>
        <p>Thank you for being part of our journey.</p>
        <p>Clara and Tom xx</p>
      </div>
      <div class="brand-mark">TALLOWMERE<br>GOODS<br>CO.</div>
      <ul class="contact">
        <li>
          <svg viewBox="0 0 12 12" aria-hidden="true"><path d="M6 1a3.3 3.3 0 0 0-3.3 3.3C2.7 6.8 6 10 6 10s3.3-3.2 3.3-5.7A3.3 3.3 0 0 0 6 1z" fill="none" stroke="currentColor" stroke-width="1.3"/><circle cx="6" cy="4.3" r="1.1" fill="currentColor"/><path d="M2 11h8" stroke="currentColor" stroke-width="1.2"/></svg>
          <span>14 Harbour Lane,<br>Hobart TAS 7004, Australia</span>
        </li>
        <li>
          <svg viewBox="0 0 12 12" aria-hidden="true"><path d="M3 1.2l1.6 2.3-1 1.1c.6 1.4 1.6 2.4 3 3l1.1-1 2.3 1.6-.8 1.8C5.4 10 2 6.6 1.2 2z" fill="currentColor"/></svg>
          <span>+61 400 512 907</span>
        </li>
        <li>
          <svg viewBox="0 0 12 12" aria-hidden="true"><g fill="none" stroke="currentColor" stroke-width="1"><circle cx="6" cy="6" r="5"/><ellipse cx="6" cy="6" rx="2.2" ry="5"/><path d="M1 6h10M2 3.3h8M2 8.7h8"/></g></svg>
          <span>tallowmeregoodsco.com.au</span>
        </li>
      </ul>
    </section>
    <section class="shopfront" role="img" aria-label="Photo of a historic sandstone shopfront with tin roof and dormer windows under tall gum trees, a hill behind and a wet road in front">
      <h2 class="shopfront-title">TALLOWMERE<br>GOODS<br>CO.</h2>
    </section>
  </main>
</body>
</html>
```